Webdesign für Quellborn Lumen Kreis e.V.
Zielgruppe
Vereinsmitglieder aus der Bio-Tech-Branche, Öffentlichkeit
Aufgabenstellung
Wir benötigen ein Webdesign für die Website des Quellborn Lumen Kreis e.V., zu liefern als PSD-Datei.

```html
<!DOCTYPE html>
<html lang="de">
<head>
<meta charset="utf-8">
<title>Quellborn Lumen Kreis e.V.</title>
<link rel="stylesheet" href="https://fonts.googleapis.com/css2?family=Arimo:wght@400;700&family=Ubuntu:wght@400;500&family=Noto+Serif&family=Cinzel:wght@400;700&display=swap">
<style>
  :root {
    --bg-teal: #22c0a8;
    --white: #ffffff;
    --ink: #333333;
    --ink-soft: #555555;
    --accent-blue: #2a9cc4;
    --hero-blue: #2a7fc0;
    --tab-green: #c5d635;
    --tab-yellow: #fdb933;
    --tab-orange: #f26522;
    --tab-text: #8a2a10;
    --menu-bg: #eef5fa;
    --menu-head: #d6e6f1;
    --rule: #e4e4e4;
    --arrow-red: #e2261c;
    --ad-orange: #f4a21c;
    --ad-green: #b8cc2c;
    --placeholder-light: #eeeeee;
    --placeholder-mid: #cfcfcf;
  }
  * { box-sizing: border-box; margin: 0; padding: 0; }
  html, body { width: 1099px; height: 1200px; overflow: hidden; }
  body { background: var(--bg-teal); font-family: "Arimo", Arial, sans-serif; color: var(--ink); position: relative; }
  .page { position: absolute; left: 70px; top: 0; width: 952px; height: 1200px; background: var(--white); }
  .abs { position: absolute; }

  .brand { left: 16px; top: 18px; display: flex; flex-direction: column; align-items: flex-start; }
  .brand-dot { width: 46px; height: 46px; border-radius: 50%; background: var(--accent-blue); margin-left: 112px; margin-bottom: 14px; }
  .brand-name { font-family: "Ubuntu", sans-serif; font-weight: 500; font-size: 16px; letter-spacing: 1.5px; color: #2b3a44; text-transform: uppercase; }

  .lang { left: 840px; top: 25px; font-size: 10px; color: #999; }
  .lang b { color: var(--accent-blue); }

  .nav { top: 67px; height: 35px; width: 119px; font-family: "Cinzel", serif; font-size: 14px; letter-spacing: 3px; color: var(--tab-text); display: flex; align-items: center; justify-content: center; }
  .nav-green { left: 463px; background: var(--tab-green); }
  .nav-yellow { left: 592px; background: var(--tab-yellow); }
  .nav-orange { left: 722px; background: var(--tab-orange); }

  .dropdown { left: 722px; top: 105px; width: 160px; z-index: 2; }
  .dropdown li { list-style: none; height: 32px; background: var(--tab-orange); border-bottom: 1px solid #f48a55; font-family: "Cinzel", serif; font-size: 14px; letter-spacing: 3px; color: var(--tab-text); padding: 8px 0 0 26px; }

  .hero { left: 0; top: 107px; width: 952px; height: 271px; background: radial-gradient(ellipse at 55% 70%, #1f7fd0 0%, #5ab4ec 30%, #cfe9fb 60%, #eef8ff 100%); }
  .hero-title { left: 62px; top: 46px; font-family: "Noto Serif", serif; font-size: 22px; line-height: 29px; color: var(--hero-blue); }
  .hero-box { left: 64px; top: 114px; width: 285px; padding: 10px 10px 8px; background: rgba(255,255,255,0.85); font-size: 10px; line-height: 13px; color: #222; text-align: justify; }

  .more::after { content: " ›"; color: var(--arrow-red); }

  .sidebar { left: 16px; top: 395px; width: 164px; }
  .menu { background: var(--menu-bg); height: 181px; }
  .menu h2 { background: var(--menu-head); font-family: "Ubuntu", sans-serif; font-weight: 400; font-size: 16px; color: var(--accent-blue); padding: 5px 16px; height: 30px; }
  .menu ul { list-style: none; padding: 14px 8px; }
  .menu li { font-family: "Ubuntu", sans-serif; font-size: 13px; color: var(--accent-blue); line-height: 24px; }
  .menu li::before { content: "› "; color: #777; }

  .search { margin-top: 19px; display: flex; align-items: center; font-size: 10px; gap: 5px; }
  .search input { width: 94px; height: 15px; border: 1px solid #999; }
  .search button { width: 32px; height: 16px; font-size: 10px; background: #f4f4f4; border: 1px solid #999; }

  .workshop { margin-top: 9px; height: 258px; border: 1px solid #9cc; background: linear-gradient(180deg, #fff 0 22%, #f6c04a 34%, #e8743a 58%, #fff 66%); position: relative; font-family: "Ubuntu", sans-serif; }
  .workshop .ws-brand { position: absolute; top: 30px; width: 100%; text-align: center; font-size: 7px; letter-spacing: 0.5px; color: #2b3a44; }
  .workshop .ws-title { position: absolute; top: 56px; right: 8px; font-size: 17px; font-weight: 500; color: #fff; }
  .workshop .ws-sub { position: absolute; top: 78px; left: 10px; font-size: 12px; line-height: 15px; color: #fff; }
  .workshop .ws-info { position: absolute; top: 176px; left: 10px; font-size: 10px; line-height: 12px; color: #333; font-weight: 500; }

  .promo { margin-top: 12px; width: 160px; height: 41px; font-family: "Ubuntu", sans-serif; color: #fff; padding: 3px 6px; overflow: hidden; }
  .promo strong { display: block; font-size: 18px; font-weight: 500; line-height: 20px; }
  .promo span { display: block; font-size: 8px; line-height: 10px; }
  .promo-news { background: var(--ad-orange); }
  .promo-cluster { background: var(--ad-green); height: 56px; margin-top: 15px; padding-top: 5px; }
  .promo-cluster span { margin-top: 3px; font-weight: 500; }

  .main { left: 224px; top: 392px; width: 704px; }
  .main h1 { font-family: "Ubuntu", sans-serif; font-weight: 400; font-size: 23px; color: #222; }
  .intro { margin-top: 9px; font-size: 10px; line-height: 13px; color: #333; }

  .col { position: absolute; width: 340px; }
  .col-left { left: 224px; }
  .col-right { left: 588px; }
  .rule { border-top: 1px solid var(--rule); }
  .col h3 { font-family: "Ubuntu", sans-serif; font-weight: 400; font-size: 14px; color: #333; letter-spacing: 0.5px; }
  .col h3.blue { color: var(--accent-blue); }

  .feature { position: relative; height: 120px; margin-top: 14px; }
  .feature-art { position: absolute; left: 0; top: 6px; width: 72px; height: 72px; border-radius: 50%; background: radial-gradient(circle at 50% 45%, var(--placeholder-light) 0%, var(--placeholder-mid) 100%); }
  .feature p { position: absolute; left: 77px; top: 6px; width: 264px; font-size: 10px; line-height: 13px; color: #333; }

  .news { margin-top: 22px; }
  .news-item { height: 107px; font-size: 10px; line-height: 13px; }
  .news-item h4 { font-family: "Ubuntu", sans-serif; font-weight: 400; font-size: 12px; color: #333; }
  .news-item .date { display: block; margin-bottom: 6px; }
  .news-item p { margin-bottom: 7px; }

  .footer { top: 1164px; font-size: 10px; color: #333; }
  .footer-left { left: 16px; }
  .footer-right { right: 16px; display: flex; gap: 9px; }
</style>
</head>
<body>
<div class="page">
  <header>
    <div class="abs brand">
      <div class="brand-dot"></div>
      <div class="brand-name">Quellborn Lumen Kreis e.V.</div>
    </div>
    <div class="abs lang"><b>DE</b> | ENG</div>
    <nav>
      <div class="abs nav nav-green">Aktueles</div>
      <div class="abs nav nav-yellow">Region</div>
      <div class="abs nav nav-orange">Service</div>
      <ul class="abs dropdown">
        <li>Jobbörse</li>
        <li>Linkliste</li>
        <li>Downloads</li>
        <li>Newsletter</li>
      </ul>
    </nav>
  </header>

  <section class="abs hero" role="img" aria-label="Blaue Wasserwelle mit glänzenden Luftblasen">
    <div class="abs hero-title">Biotechnology is a field of applied biology<br>that involves the use of living</div>
    <div class="abs hero-box">Deutschland bewiesen, was wir gemeinsam leisten können, wenn es darauf ankommt. Daher haben wir auch allen Grund, dem Jahr 2011 optimistisch entgegen­zusehen.“ <span class="more">mehr</span></div>
  </section>

  <aside class="abs sidebar">
    <div class="menu">
      <h2>Menu</h2>
      <ul>
        <li>Start</li>
        <li>Über uns</li>
        <li>Veranstaltungen</li>
        <li>Kontakt</li>
        <li>Impresum</li>
      </ul>
    </div>
    <form class="search"><label>Suche:</label><input type="text"><button type="button">go</button></form>
    <div class="workshop" role="img" aria-label="Workshop-Banner mit warmem Farbverlauf">
      <div class="ws-brand">QUELLBORN LUMEN KREIS E.V.</div>
      <div class="ws-title">Workshop</div>
      <div class="ws-sub">Pharmaindustrie im<br>Wandel: Was sind die<br>Erfolgsfaktoren?</div>
      <div class="ws-info">Dienstag I 14. Dezember 2010<br>17.00 bis ca. 19:45 Uhr<br><br>Haus der Wirtschaft Quellborn<br>Lindenhof 12<br>60999 Quellborn</div>
    </div>
    <div class="promo promo-news"><strong>Newletter @</strong><span>Hier anmelden! →</span></div>
    <div class="promo promo-cluster"><strong>Clusterkonzept</strong><span>„Integrierte Bioindustrie<br>Quellborn“</span></div>
  </aside>

  <main class="abs main">
    <h1>Willkommen</h1>
    <p class="intro">Der Quellborn Lumen Kreis ist ein Zusammen-schluß von Wissenschaftlern, Unternehmern und Dienst-leistern, die die biotechno-logische Forschung in der Region Quellborn /Rhein-Main voranbringen wollen. Wir sind qualifizierter Ansprech-partner wenn es darum geht, Forschungsideen zu bewerten, umzusetzen und zu kommunizieren. Dazu bieten wir Plattformen und Arbeitskreise an und führen selbst Studien durch.</p>
  </main>

  <section class="col col-left" style="top:502px">
    <div class="rule" style="padding-top:20px"><h3>MEDIZINTECHNIK / PHARMA</h3></div>
    <div class="feature">
      <div class="feature-art" role="img" aria-label="Platz für Themenbild Medizintechnik"></div>
      <p>Sed diam nonummy nibh euismod tincidunt ut laoreet dolore magna aliquam erat volutpat. Ut wisi enim ad minim veniam, quis nostrud exerci tation ullamcorper suscipit lobortis nisl ut aliquip. incidunt ut laoreet dolore magna aliquam erat volutpat. Ut wisi enim ad minim veniam, quis nostrud exerci tation ullamcorper.<br><span class="more">mehr</span></p>
    </div>
  </section>
  <section class="col col-right" style="top:502px">
    <div class="rule" style="padding-top:20px"><h3>MEDIZINTECHNIK / PHARMA</h3></div>
    <div class="feature">
      <div class="feature-art" role="img" aria-label="Platz für Themenbild Pharma"></div>
      <p>Sed diam nonummy nibh euismod tincidunt ut laoreet dolore magna aliquam erat volutpat. Ut wisi enim ad minim veniam, quis nostrud exerci tation ullamcorper suscipit lobortis nisl ut aliquip. incidunt ut laoreet dolore magna aliquam erat volutpat. Ut wisi enim ad minim veniam, quis nostrud exerci tation ullamcorper.<br><span class="more">mehr</span></p>
    </div>
  </section>

  <section class="col col-left" style="top:707px">
    <div class="rule" style="padding-top:22px"><h3 class="blue">AKTUELLES</h3></div>
    <div class="news">
      <article class="news-item"><h4>MELDUNG 1</h4><span class="date">07.12.10</span><p>Sed diam nonummy nibh euismod tincidunt ut laoreet dolore magna aliquam erat volutpat. Ut wisi enim ad minim veniam, quis nostrud exerci</p><span class="more">zum Thema</span></article>
      <article class="news-item"><h4>MELDUNG 2</h4><span class="date">07.12.10</span><p>Sed diam nonummy nibh euismod tincidunt ut laoreet dolore magna aliquam erat volutpat. Ut wisi enim ad minim veniam, quis nostrud exerci</p><span class="more">zum Thema</span></article>
      <article class="news-item"><h4>MELDUNG 3</h4><span class="date">07.12.10</span><p>Sed diam nonummy nibh euismod tincidunt ut laoreet dolore magna aliquam erat volutpat. Ut wisi enim ad minim veniam, quis nostrud exerci</p><span class="more">zum Thema</span></article>
    </div>
  </section>
  <section class="col col-right" style="top:707px">
    <div class="rule" style="padding-top:22px"><h3 class="blue">VERANSTALTUNGEN</h3></div>
    <div class="news">
      <article class="news-item"><h4>NUMMER 1</h4><span class="date">07.12.10</span><p>Sed diam nonummy nibh euismod tincidunt ut laoreet dolore magna aliquam erat volutpat. Ut wisi enim ad minim veniam, quis nostrud exerci</p><span class="more">zum Thema</span></article>
      <article class="news-item"><h4>NUMMER 2</h4><span class="date">07.12.10</span><p>Sed diam nonummy nibh euismod tincidunt ut laoreet dolore magna aliquam erat volutpat. Ut wisi enim ad minim veniam, quis nostrud exerci</p><span class="more">zum Thema</span></article>
      <article class="news-item"><h4>NUMMER 2</h4><span class="date">07.12.10</span><p>Sed diam nonummy nibh euismod tincidunt ut laoreet dolore magna aliquam erat volutpat. Ut wisi enim ad minim veniam, quis nostrud exerci</p><span class="more">zum Thema</span></article>
    </div>
  </section>

  <footer>
    <div class="abs footer footer-left">© 2008-2010 www.quellborn-kreis.de</div>
    <div class="abs footer footer-right"><span>Home</span><span>Impressum</span><span>Sitemap</span></div>
  </footer>
</div>
</body>
</html>
```